Multi Disciplinary Health Clinic Needs a Pop Up Banner

Brightway Health needs a pop up banner ( approx. 33" x 80") to use at marketing events. We offer Chiropractic, Massage Therapy, Acupuncture, Laser Therapy, Shockwave Therapy and a lot of other modalities. We have a diverse client base ranging from children to professional athletes. More info about our clinic can be found at www.brightwayhealth.ca

Target Market(s)

potential patients, all age ranges, people who are in pain or are wanting to improve their health

Industry/Entity Type

Health And Wellness

Font styles to use
Sans Serif

Requirements
Must have
• our logo
• serives: chiropractic, massage therapy, shockwave, laser
• our logo colours as the basis for the colour theme
• our website address
Nice to have
• our phone number
• images from our website ( i have high resolution files of all images)
• word font that fits with our logo font
Should not have
• an abundance of spa massage pictures. we focus more on the rehabilitation of pain and injury.

```html
<!DOCTYPE html>
<html lang="en">
<head>
<meta charset="utf-8">
<title>Brightway Health – Pop Up Banner</title>
<link href="https://fonts.googleapis.com/css2?family=Arimo:wght@400;700&display=swap" rel="stylesheet">
<style>
  :root {
    --brand-blue: #0f6cb3;
    --brand-blue-light: #1c80c8;
    --brand-blue-dark: #0b5a98;
    --logo-blue: #1a5fa6;
    --steel-grey: #5d6770;
    --white: #ffffff;
    --photo-warm-1: #f6e2cc;
    --photo-warm-2: #e9b68c;
    --photo-warm-3: #c9835a;
  }
  * { box-sizing: border-box; margin: 0; padding: 0; }
  html, body { width: 1200px; height: 2908px; overflow: hidden; }
  body { font-family: "Arimo", Arial, sans-serif; background: var(--white); }

  .banner {
    position: relative;
    width: 1200px;
    height: 2908px;
    overflow: hidden;
    background: radial-gradient(ellipse at 50% 55%, var(--brand-blue-light) 0%, var(--brand-blue) 55%, var(--brand-blue-dark) 100%);
  }

  .hero-photo {
    position: absolute;
    left: 0; top: 0;
    width: 1200px; height: 1700px;
    background:
      linear-gradient(to bottom, #fff 0px, #fff 150px, rgba(255,255,255,0) 330px),
      radial-gradient(ellipse at 60% 45%, var(--photo-warm-2) 0%, var(--photo-warm-1) 45%, #f3efe9 80%),
      linear-gradient(135deg, var(--photo-warm-3), var(--photo-warm-1));
  }

  .brand {
    position: absolute;
    left: 0; top: 92px;
    width: 1200px;
    display: flex;
    justify-content: center;
    align-items: center;
    gap: 24px;
  }
  .brand-dot {
    width: 64px; height: 64px;
    border-radius: 50%;
    background: var(--logo-blue);
  }
  .brand-name {
    font-weight: 700;
    font-size: 92px;
    color: var(--logo-blue);
    letter-spacing: 1px;
  }

  .panel-shape { position: absolute; left: 0; top: 0; }

  .services-tab {
    position: absolute;
    left: 0; top: 1086px;
    width: 815px; height: 86px;
    background: var(--white);
    clip-path: polygon(0 0, 770px 0, 815px 86px, 0 86px);
    box-shadow: 0 4px 8px rgba(0,0,0,.25);
  }
  .services-title {
    position: absolute;
    left: 22px; top: 1105px;
    font-weight: 700;
    font-size: 44px;
    color: var(--logo-blue);
    letter-spacing: .5px;
  }

  .service-list {
    position: absolute;
    list-style: none;
    color: var(--white);
    font-weight: 700;
    font-size: 45px;
  }
  .service-list li {
    height: 121px;
    position: relative;
    padding-left: 42px;
    line-height: 50px;
    white-space: nowrap;
  }
  .service-list li::before {
    content: "";
    position: absolute;
    left: 4px; top: 20px;
    width: 12px; height: 12px;
    border-radius: 50%;
    background: var(--white);
  }
  .service-list.col-left { left: 64px; top: 1303px; }
  .service-list.col-right { left: 546px; top: 1303px; }

  .photo-strip { position: absolute; left: 0; top: 1977px; width: 1200px; height: 281px; display: flex; }
  .strip-photo { flex: 1; height: 100%; }
  .strip-photo.treatment { background: linear-gradient(135deg, #f4f1ee, #e6c2a6 60%, #f7f5f3); }
  .strip-photo.wellness { background: linear-gradient(160deg, #d7b58c, #b88a5c 55%, #8a6a48); border-left: 3px solid #fff; border-right: 3px solid #fff; }
  .strip-photo.water { background: radial-gradient(ellipse at 55% 45%, #b7b1a4, #4f5a4a 60%, #2e3a2e); }

  .strip-frame { position: absolute; left: 0; top: 1920px; }

  .contact {
    position: absolute;
    left: 0; width: 1200px;
    text-align: center;
    color: var(--white);
    font-weight: 700;
  }
  .contact-lead { top: 2375px; font-size: 42px; }
  .contact-line {
    display: flex; justify-content: center; align-items: center; gap: 26px;
    font-size: 58px;
  }
  .contact-line svg { flex: none; }
  .contact-phone { top: 2512px; }
  .contact-email { top: 2636px; }
  .contact-web { top: 2758px; }
</style>
</head>
<body>
<div class="banner">

  <div class="hero-photo" role="img" aria-label="Photo of a client relaxing on a treatment table while a therapist works on her shoulders"></div>

  <div class="brand">
    <span class="brand-dot"></span>
    <span class="brand-name">Brightway Health</span>
  </div>

  <svg class="panel-shape" width="1200" height="2000" viewBox="0 0 1200 2000" aria-hidden="true">
    <path d="M0,775 C560,782 1060,1000 1200,1400 L1200,2000 L0,2000 Z" fill="var(--steel-grey)"/>
    <path d="M0,868 C560,870 1060,1160 1200,1660 L1200,2000 L0,2000 Z" fill="var(--brand-blue)"/>
    <path d="M0,868 C560,870 1060,1160 1200,1660" fill="none" stroke="#ffffff" stroke-width="5"/>
  </svg>

  <div class="services-tab"></div>
  <h2 class="services-title">GENERAL SERVICES OFFERED</h2>

  <ul class="service-list col-left">
    <li>Chiropractic</li>
    <li>Massage</li>
    <li>Acupuncture</li>
    <li>Shockwave</li>
    <li>Laser Therapy</li>
  </ul>
  <ul class="service-list col-right">
    <li>Active Release</li>
    <li>Kinesiology Tape</li>
    <li>Scraping Technology</li>
    <li>Cupping Technology</li>
  </ul>

  <div class="photo-strip">
    <div class="strip-photo treatment" role="img" aria-label="Photo of acupuncture needles placed on a hand"></div>
    <div class="strip-photo wellness" role="img" aria-label="Photo of soap bars, a rolled towel and a basket on a wooden mat"></div>
    <div class="strip-photo water" role="img" aria-label="Photo of feet resting in clear water"></div>
  </div>

  <svg class="strip-frame" width="1200" height="380" viewBox="0 0 1200 380" aria-hidden="true">
    <path d="M0,0 L1200,0 L1200,57 Q600,20 0,57 Z" fill="var(--brand-blue)"/>
    <path d="M0,55 Q600,18 1200,55" fill="none" stroke="#ffffff" stroke-width="6"/>
    <path d="M0,338 L0,380 L1200,380 L1200,338 Q600,392 0,338 Z" fill="var(--brand-blue)"/>
    <path d="M0,338 Q600,392 1200,338" fill="none" stroke="var(--steel-grey)" stroke-width="14"/>
    <path d="M0,346 Q600,400 1200,346" fill="none" stroke="#ffffff" stroke-width="4"/>
  </svg>

  <p class="contact contact-lead">For More Information Please Contact Us:</p>

  <p class="contact contact-line contact-phone">
    <svg width="48" height="40" viewBox="0 0 48 40" aria-hidden="true">
      <path d="M4,10 Q24,-2 44,10 L42,17 L33,15 L32,10 Q24,7 16,10 L15,15 L6,17 Z" fill="#fff"/>
      <path d="M12,18 L36,18 L44,38 L4,38 Z" fill="#fff"/>
      <circle cx="24" cy="28" r="5" fill="var(--brand-blue)"/>
    </svg>
    <span>(403) 555-0142</span>
  </p>

  <p class="contact contact-line contact-email">
    <svg width="50" height="34" viewBox="0 0 50 34" aria-hidden="true">
      <rect x="2" y="2" width="46" height="30" fill="none" stroke="#fff" stroke-width="4"/>
      <path d="M2,2 L25,20 L48,2" fill="none" stroke="#fff" stroke-width="4"/>
    </svg>
    <span>info@brightwayhealth.ca</span>
  </p>

  <p class="contact contact-line contact-web">
    <svg width="46" height="46" viewBox="0 0 46 46" aria-hidden="true">
      <circle cx="23" cy="23" r="20" fill="none" stroke="#fff" stroke-width="4"/>
      <ellipse cx="23" cy="23" rx="9" ry="20" fill="none" stroke="#fff" stroke-width="3"/>
      <path d="M3,23 H43 M7,13 H39 M7,33 H39" stroke="#fff" stroke-width="3"/>
    </svg>
    <span>http://www.brightwayhealth.ca/</span>
  </p>

</div>
</body>
</html>
```